RW Frameworks Inc Business cards

We need business cards using our existing logo but slightly modified. Right now the logo says RW Framework Masonry. We want to keep the RW part of the design, but replace the Framework Masonry portion with "FRAMEWORKS". Please see the attached file.
Ideally this would be a blank template so we can add Different Names, titles, and phone numbers later.
On the one side we want only the logo and on the other side the detail. I'm attaching an example for you to see.
Please reach out with any other questions. Our address and other details will be given out once we find a design we like.

Target Market(s)

Construction Industry

```html
<!DOCTYPE html>
<html lang="en">
<head>
<meta charset="UTF-8">
<title>RW Frameworks Inc — Business Cards</title>
<link rel="stylesheet" href="https://fonts.googleapis.com/css2?family=Montserrat:wght@600&family=Roboto:wght@400;700&display=swap">
<style>
  :root {
    --backdrop: #5a82bc;
    --brand-blue: #2e62a3;
    --card-white: #f2f2f2;
    --text-grey: #4a4a4a;
    --strip-grey: #7b7b7b;
    --white: #ffffff;
  }
  * { box-sizing: border-box; margin: 0; padding: 0; }
  html, body { width: 1200px; height: 852px; overflow: hidden; }
  body {
    background: var(--backdrop);
    font-family: "Roboto", Arial, sans-serif;
    position: relative;
  }
  .card {
    position: absolute;
    width: 500px;
    height: 286px;
    border-radius: 22px;
    overflow: hidden;
  }
  .card--front {
    left: 110px; top: 120px;
    background: var(--brand-blue);
    display: flex; align-items: center; justify-content: center;
  }
  .card--back {
    left: 590px; top: 450px;
    background: var(--card-white);
  }
  .brand-name {
    font-family: "Montserrat", Arial, sans-serif;
    font-weight: 600;
    letter-spacing: 4px;
    white-space: nowrap;
  }
  .card--front .brand-name { color: var(--white); font-size: 36px; }
  .card--back .brand-name {
    position: absolute; left: 34px; top: 118px;
    color: var(--brand-blue); font-size: 22px; letter-spacing: 3px;
  }
  .details {
    position: absolute; left: 300px; top: 40px;
    color: var(--text-grey);
  }
  .person-name { color: var(--brand-blue); font-weight: 700; font-size: 18px; }
  .person-title { font-size: 12px; margin: 2px 0 16px 16px; }
  .contact-list { list-style: none; font-size: 12px; line-height: 17px; }
  .contact-list li { display: flex; gap: 8px; align-items: flex-start; }
  .contact-list svg { width: 11px; height: 11px; margin-top: 3px; fill: var(--brand-blue); flex: none; }
  .address { margin: 4px 0 0 19px; font-size: 12px; line-height: 17px; }
  .base-strip {
    position: absolute; left: 0; right: 0; bottom: 0; height: 12px;
    background: var(--strip-grey);
  }
  .tagline-tab {
    position: absolute; right: 0; bottom: 0;
    width: 230px; height: 44px;
    background: var(--brand-blue);
    border-top-left-radius: 16px;
    color: var(--white); font-weight: 700; font-size: 13px;
    display: flex; align-items: center; justify-content: center;
    padding-bottom: 4px;
  }
</style>
</head>
<body>
  <section class="card card--front">
    <span class="brand-name">RW FRAMEWORKS</span>
  </section>

  <section class="card card--back">
    <span class="brand-name">RW FRAMEWORKS</span>
    <div class="details">
      <p class="person-name">Mark RW Ellison</p>
      <p class="person-title">Managing Director</p>
      <ul class="contact-list">
        <li><svg viewBox="0 0 12 12"><path d="M1 3c0-1 1-2 2-2h6c1 0 2 1 2 2v1H8V3H4v1H1zM2 5h8l1 6H1z"/></svg>541-208-3374</li>
        <li><svg viewBox="0 0 12 12"><path d="M0 2h12v8H0zM1 3l5 4 5-4v-.2H1z" fill-rule="evenodd"/></svg>mark@rwframeworks.net</li>
        <li><svg viewBox="0 0 12 12"><circle cx="6" cy="6" r="5.5"/><path d="M0.5 6h11M6 .5v11" stroke="#f2f2f2" stroke-width="1"/></svg>www.rwframeworks.net</li>
      </ul>
      <p class="address">418 Harbor Ln., Fairview,<br>Oregon, US 97024</p>
    </div>
    <div class="base-strip"></div>
    <div class="tagline-tab">RW Framework Masonry</div>
  </section>
</body>
</html>
```